Drowsy Heron

Need a business card for our restaurant. Restaurant and Bar in the mountains of North Idaho. Rustic looking card

Contact Information for Business Card

rustic design, wood and metal looking, primarily neutral colors

Requirements
Must have
• Name, address, phone number, website, email address

```html
<!DOCTYPE html>
<html lang="en">
<head>
<meta charset="utf-8">
<title>The Drowsy Heron – Business Card</title>
<link href="https://fonts.googleapis.com/css2?family=Rokkitt:wght@300;400;600;800&family=Archivo:wght@600&display=swap" rel="stylesheet">
<style>
  :root {
    --page-bg: #b7aa9c;
    --brick-dark: #6e3a26;
    --brick-mid: #a4512f;
    --brick-light: #b9694a;
    --wood-light: #dcb56a;
    --wood-mid: #c99a4a;
    --wood-dark: #b58338;
    --ink-brown: #4a2d0e;
    --badge-white: #f7f5f1;
    --badge-ink: #111111;
    --label-white: #ffffff;
  }
  * { box-sizing: border-box; margin: 0; padding: 0; }
  html, body { width: 675px; height: 1200px; overflow: hidden; }
  body {
    background: var(--page-bg);
    font-family: "Rokkitt", serif;
    position: relative;
  }
  .card {
    position: absolute;
    left: 57px;
    width: 560px;
    height: 353px;
    overflow: hidden;
    box-shadow: 0 6px 14px rgba(0,0,0,0.25);
  }
  .card--back { top: 150px; }
  .card--front { top: 620px; }
  .card__texture { position: absolute; inset: 0; }
  .card__texture--brick {
    background: linear-gradient(135deg, var(--brick-light) 0%, var(--brick-mid) 45%, var(--brick-dark) 100%);
  }
  .card__texture--wood {
    background: linear-gradient(100deg, var(--wood-mid) 0%, var(--wood-light) 40%, var(--wood-mid) 70%, var(--wood-dark) 100%);
  }
  .badge {
    position: absolute;
    left: 50%; top: 50%;
    width: 204px; height: 204px;
    margin: -102px 0 0 -102px;
    border-radius: 50%;
    background: var(--badge-white);
    display: flex; flex-direction: column;
    align-items: center; justify-content: center;
    text-align: center;
  }
  .badge__name {
    font-family: "Rokkitt", serif;
    font-weight: 400;
    font-size: 26px;
    line-height: 1.1;
    letter-spacing: 2px;
    text-transform: uppercase;
    color: var(--badge-ink);
  }
  .brand { position: absolute; left: 32px; top: 44px; color: var(--ink-brown); }
  .brand__name {
    font-weight: 300;
    font-size: 23px;
    letter-spacing: 1px;
    text-transform: uppercase;
  }
  .brand__tagline {
    font-weight: 300;
    font-size: 10px;
    letter-spacing: 7px;
    text-transform: uppercase;
    margin-top: 1px;
  }
  .person { position: absolute; left: 30px; top: 172px; color: var(--ink-brown); }
  .person__name {
    font-weight: 800;
    font-size: 34px;
    line-height: 1;
    letter-spacing: 1px;
    text-transform: uppercase;
  }
  .person__title {
    font-weight: 300;
    font-size: 16px;
    text-transform: uppercase;
    margin-top: -2px;
  }
  .contact { position: absolute; left: 30px; top: 257px; list-style: none; color: var(--ink-brown); }
  .contact__item {
    display: flex; align-items: center; gap: 8px;
    font-weight: 600;
    font-size: 15.5px;
    line-height: 18px;
  }
  .contact__icon { width: 13px; height: 13px; flex: none; fill: none; stroke: var(--ink-brown); stroke-width: 2; }
  .label {
    position: absolute;
    left: 57px; width: 560px;
    text-align: center;
    font-family: "Archivo", sans-serif;
    font-weight: 600;
    font-size: 12px;
    letter-spacing: 1.5px;
    color: var(--label-white);
  }
  .label--back { top: 522px; }
  .label--front { top: 992px; }
</style>
</head>
<body>

  <section class="card card--back" aria-label="Back side of business card">
    <div class="card__texture card__texture--brick" role="img" aria-label="Weathered red brick wall texture"></div>
    <div class="badge">
      <span class="badge__name">The Drowsy<br>Heron</span>
    </div>
  </section>
  <p class="label label--back">BACK SIDE DESIGN</p>

  <section class="card card--front" aria-label="Front side of business card">
    <div class="card__texture card__texture--wood" role="img" aria-label="Warm light wood grain texture"></div>

    <header class="brand">
      <p class="brand__name">The Drowsy Heron</p>
      <p class="brand__tagline">Restaurant &amp; Bar</p>
    </header>

    <div class="person">
      <p class="person__name">John Doe</p>
      <p class="person__title">General Manager</p>
    </div>

    <ul class="contact">
      <li class="contact__item">
        <svg class="contact__icon" viewBox="0 0 14 14"><path d="M7 13 C3 8 2.5 6.5 2.5 5 A4.5 4.5 0 0 1 11.5 5 C11.5 6.5 11 8 7 13Z"/><circle cx="7" cy="5" r="1.6"/></svg>
        742 Cedar Ridge Rd, Pinecrest, ID 83899
      </li>
      <li class="contact__item">
        <svg class="contact__icon" viewBox="0 0 14 14"><path d="M3 1.5 L5.5 4 L4 5.8 C5 8 6 9 8.2 10 L10 8.5 L12.5 11 L11 12.5 C6 12.5 1.5 8 1.5 3Z"/></svg>
        (208) 555-0147
      </li>
      <li class="contact__item">
        <svg class="contact__icon" viewBox="0 0 14 14"><rect x="1.5" y="3" width="11" height="8"/><path d="M1.5 3 L7 7.5 L12.5 3"/></svg>
        hello@thedrowsyheronpinecrest.com
      </li>
      <li class="contact__item">
        <svg class="contact__icon" viewBox="0 0 14 14"><circle cx="7" cy="7" r="5.5"/><ellipse cx="7" cy="7" rx="2.4" ry="5.5"/><path d="M1.5 7 H12.5"/></svg>
        thedrowsyheronpinecrest.com
      </li>
    </ul>
  </section>
  <p class="label label--front">FRONT SIDE DESIGN</p>

</body>
</html>
```